hillcrest coolant & muffler (the gear for every motoring job)

we need a business card design for a company that started out as a radiator shop cleaning repairing recoring or selling new radiators. then we got into fuel tank repair cleaning repairing and lining if the tank leaks we fix it if it has jelled gas or rust we clean it then roll a liner in it no more fuel touching the tank.later we started doing exhaust from small single exhaust to custom duels.now the first of the year we started selling and repairing tires. Now we are doing alignments . we also do brakes and suspension and oil changes we need some way to get the message out about all we do.I would like to see some flare in the writing of the name of the business but still easily read.read. I'm thinking on black and red as colors.but im open for suggestions Id like it to be eye catching and memorable.
Updates

Project Deadline Extended
Reason: i dont have a logo for you please make me one

Target Market(s)

4 wheel alignment-tires new and used.radiator clean and repair recores new complete radiators.fuel tank cleaning and repair and liners.exhaust standard single and custom duels.cars,trucks, and buses.from the youngest driver to the oldest.

Industry/Entity Type

Automotive

Contact Information for Business Card

Hillcrest Coolant & Muffler Inc. 418 S Pembrook lane Marlow in.46902 574-208-6143 m-f 9-5 sat 9-12 for tires call 812-365-9497m-f8-5 sat8-12

Font styles to use
Decorative

Colors
000000
ec1f27

Requirements
Must have
• eye catching colors and letters. both phone numbers and hours.logo
Nice to have
• list of things we can do

```html
<!DOCTYPE html>
<html lang="en">
<head>
<meta charset="utf-8">
<title>Hillcrest Coolant &amp; Muffler Inc. — Business Card</title>
<link rel="stylesheet" href="https://fonts.googleapis.com/css2?family=Saira:wght@400;500&display=swap">
<style>
  :root {
    --ink: #000000;
    --ink-soft: #2b2b2b;
    --paper: #f4f4f4;
    --red: #ec1f27;
    --rule: #9a9a9a;
    --stage: #e6e4e0;
    --white: #ffffff;
  }
  * { box-sizing: border-box; margin: 0; padding: 0; }
  html, body {
    width: 1200px; height: 902px; overflow: hidden;
    background: var(--stage);
    font-family: "Saira", sans-serif;
  }
  .canvas {
    position: relative; width: 1200px; height: 902px;
  }
  .card {
    position: absolute; left: 260px; width: 680px; height: 388px;
    background: var(--paper); overflow: hidden;
    box-shadow: 0 6px 18px rgba(0,0,0,.18);
  }
  .card--front { top: 42px; }
  .card--back { top: 472px; }

  .band { position: absolute; left: 0; width: 100%; background: var(--ink); }
  .band--top { top: 0; height: 56px; }
  .band--bottom { bottom: 0; height: 56px; }

  /* front */
  .front-name {
    position: absolute; left: 110px; top: 120px;
    display: flex; align-items: center; gap: 22px;
    color: var(--ink-soft); font-weight: 500;
  }
  .brand-square { width: 46px; height: 46px; background: var(--red); flex: none; }
  .front-name .title { font-size: 74px; line-height: .9; letter-spacing: -1px; }
  .front-name .sub { font-size: 34px; line-height: 1.2; }

  /* back */
  .card--back .band--top { height: 42px; }
  .name-panel {
    position: absolute; left: 0; top: 0; width: 330px; height: 128px;
    background: var(--ink); color: var(--white); font-weight: 500;
    padding: 34px 0 0 30px;
  }
  .name-panel .title { font-size: 50px; line-height: .95; letter-spacing: -.5px; }
  .name-panel .sub { font-size: 21px; line-height: 1.3; }
  .back-mark {
    position: absolute; left: 150px; top: 170px;
    width: 70px; height: 70px; background: var(--red);
  }
  .divider {
    position: absolute; left: 372px; top: 120px; width: 1px; height: 150px;
    background: var(--rule);
  }
  .contact {
    position: absolute; left: 400px; top: 86px; width: 250px;
    list-style: none; color: var(--ink-soft); font-size: 17px; line-height: 1.2;
  }
  .contact li {
    display: flex; align-items: flex-start; gap: 10px;
    padding: 8px 0 6px; border-bottom: 1px solid var(--rule);
  }
  .contact li:first-child { border-top: 1px solid var(--rule); }
  .contact svg { width: 12px; height: 14px; margin-top: 3px; flex: none; fill: var(--red); }
  .card--back .band--bottom { height: 84px; }
  .hours {
    position: absolute; left: 30px; bottom: 12px;
    color: var(--white); font-size: 19px; line-height: 1.45;
  }
  .hours span { display: inline-block; margin-right: 18px; }
  .hours .tires { font-size: 15px; }
</style>
</head>
<body>
<main class="canvas">
  <section class="card card--front" aria-label="Card front">
    <div class="band band--top"></div>
    <div class="front-name">
      <div class="brand-square"></div>
      <div>
        <div class="title">Hillcrest</div>
        <div class="sub">Coolant &amp; Muffler Inc</div>
      </div>
    </div>
    <div class="band band--bottom"></div>
  </section>

  <section class="card card--back" aria-label="Card back">
    <div class="band band--top"></div>
    <div class="name-panel">
      <div class="title">Hillcrest</div>
      <div class="sub">Coolant &amp; Muffler Inc</div>
    </div>
    <div class="back-mark"></div>
    <div class="divider"></div>
    <ul class="contact">
      <li><svg viewBox="0 0 12 14"><path d="M2 1l3 0 1 3-2 1.5c.8 2 2 3.2 3.5 4L9 7.5l3 1v3L10.5 13C5 12 1 7 1 2z"/></svg>574-208-6143</li>
      <li><svg viewBox="0 0 12 14"><path d="M2 1l3 0 1 3-2 1.5c.8 2 2 3.2 3.5 4L9 7.5l3 1v3L10.5 13C5 12 1 7 1 2z"/></svg>574-208-7381</li>
      <li><svg viewBox="0 0 12 14"><path d="M6 0a5 5 0 0 0-5 5c0 3.5 5 9 5 9s5-5.5 5-9a5 5 0 0 0-5-5zm0 7a2 2 0 1 1 0-4 2 2 0 0 1 0 4z"/></svg><span>418 S Pembrook lane<br>Marlow in.46902</span></li>
    </ul>
    <div class="band band--bottom"></div>
    <div class="hours">
      <div><span>mon - fri 9 - 5</span><span>sat 9 - 12</span><span class="tires">for tires call</span></div>
      <div><span>mon - fri 8 - 5</span><span>sat 8 - 12</span><span class="tires">for tires call</span></div>
    </div>
  </section>
</main>
</body>
</html>
```